Bright Lantern,

Tri-fold brochure. This brochure is designed to get attention from college students who wish to get hands-on broadcast and online experience and do so covering interesting stories and people in places traditional media does not go. I'll be their professor and adviser. Would like the brochure as a single fold using 8.5 X 11 although I would appreciate any suggestions on size or number of folds.

I'm interested in a design the designer is interested in. Love passion. You can see I have this brochure generally mapped out, but I am not stuck on photo placement. I don't care if a photo stretches 2 or 3 pages. I'm interested in other design elements besides my photos and copy.

I've included several photos that can be used. The only photo I'm stuck on is the Peter Vallory Building for the front page. It's a B&W page completely except for the Chicago flag at the bottom.

```html
<!DOCTYPE html>
<html lang="en">
<head>
<meta charset="utf-8">
<title>Bright Lantern – Brochure Inside Spread</title>
<link href="https://fonts.googleapis.com/css2?family=Roboto+Slab:wght@300;700&display=swap" rel="stylesheet">
<style>
  :root {
    --ink: #0b0b0c;
    --panel-dark: #141416;
    --brand-blue: #0a6fc2;
    --sky-blue: #3a8fe0;
    --ring-blue: #5aa8e6;
    --ring-white: #ffffff;
    --text: #ffffff;
    --fog-light: #d2d2d2;
    --fog-dark: #6a6a6a;
  }
  * { box-sizing: border-box; margin: 0; padding: 0; }
  html, body { width: 1200px; height: 927px; overflow: hidden; background: var(--ink); }
  .spread { position: relative; width: 1200px; height: 927px; overflow: hidden;
    background: linear-gradient(135deg, #1a1a1c 0%, var(--ink) 45%, #19191b 100%); }
  .spread__art { position: absolute; inset: 0; }
  .feature { position: absolute; color: var(--text); font-family: "Roboto Slab", Georgia, serif; }
  .feature__title { font-weight: 700; font-size: 27px; line-height: 1.1; margin-bottom: 14px; letter-spacing: 0.2px; }
  .feature__body { font-weight: 300; font-size: 15.6px; line-height: 1.08; margin-bottom: 12px; }
  .feature--intro { left: 57px; top: 114px; width: 336px; }
  .feature--social { left: 663px; top: 333px; width: 500px; }
  .feature--location { left: 266px; top: 460px; width: 282px; }
  .feature--closing { left: 56px; top: 747px; width: 336px; }
</style>
</head>
<body>
<main class="spread">
  <svg class="spread__art" width="1200" height="927" viewBox="0 0 1200 927">
    <defs>
      <linearGradient id="commuterTone" x1="0" y1="0" x2="1" y2="1">
        <stop offset="0" stop-color="#4ea3ef"/><stop offset="1" stop-color="#1f6fc0"/>
      </linearGradient>
      <linearGradient id="skylineTone" x1="0" y1="0" x2="0" y2="1">
        <stop offset="0" stop-color="var(--fog-light)"/><stop offset="0.6" stop-color="#8a8a8a"/><stop offset="1" stop-color="#bdbdbd"/>
      </linearGradient>
      <linearGradient id="muralTone" x1="0" y1="0" x2="1" y2="1">
        <stop offset="0" stop-color="#9a6a4a"/><stop offset="0.5" stop-color="#2f8f7a"/><stop offset="1" stop-color="#b0684a"/>
      </linearGradient>
      <linearGradient id="musicianTone" x1="0" y1="0" x2="1" y2="1">
        <stop offset="0" stop-color="#8a5a3a"/><stop offset="1" stop-color="#1c1c1c"/>
      </linearGradient>
      <linearGradient id="platformTone" x1="0" y1="0" x2="0" y2="1">
        <stop offset="0" stop-color="#b8473a"/><stop offset="0.45" stop-color="#7a7f8a"/><stop offset="1" stop-color="#2c2f38"/>
      </linearGradient>
      <linearGradient id="foodTone" x1="0" y1="0" x2="1" y2="1">
        <stop offset="0" stop-color="#e2c48a"/><stop offset="0.5" stop-color="#a8442e"/><stop offset="1" stop-color="#8fae3c"/>
      </linearGradient>
      <linearGradient id="fountainTone" x1="0" y1="0" x2="1" y2="1">
        <stop offset="0" stop-color="#5e7a52"/><stop offset="0.6" stop-color="#8a6a5c"/><stop offset="1" stop-color="#3a5c8a"/>
      </linearGradient>
    </defs>

    <rect class="panel-dark" x="600" y="0" width="600" height="927" fill="var(--panel-dark)"/>

    <polygon role="img" aria-label="Photo: commuter checking a phone on a train platform, blue tint"
      points="600,0 1200,0 1200,186 600,322" fill="url(#commuterTone)"/>

    <polygon class="wedge-blue" points="600,324 190,446 168,684 600,760" fill="var(--brand-blue)"/>

    <polygon role="img" aria-label="Photo: city skyline rising above fog, black and white"
      points="600,478 1200,665 1200,927 600,927" fill="url(#skylineTone)"/>

    <g class="photo-circle">
      <circle cx="522" cy="120" r="148" fill="var(--ring-blue)"/>
      <circle cx="522" cy="120" r="145" fill="var(--ring-white)"/>
      <circle role="img" aria-label="Photo: colourful street mural" cx="522" cy="120" r="139" fill="url(#muralTone)"/>
    </g>
    <g class="photo-circle">
      <circle cx="1090" cy="120" r="140" fill="var(--ring-blue)"/>
      <circle cx="1090" cy="120" r="137" fill="var(--ring-white)"/>
      <circle role="img" aria-label="Photo: street musician playing trumpet" cx="1090" cy="120" r="131" fill="url(#musicianTone)"/>
    </g>
    <g class="photo-circle">
      <circle cx="112" cy="556" r="124" fill="var(--ring-blue)"/>
      <circle cx="112" cy="556" r="121" fill="var(--ring-white)"/>
      <circle role="img" aria-label="Photo: crowd on an elevated train platform" cx="112" cy="556" r="115" fill="url(#platformTone)"/>
    </g>
    <g class="photo-circle">
      <circle cx="568" cy="772" r="104" fill="var(--ring-blue)"/>
      <circle cx="568" cy="772" r="101" fill="var(--ring-white)"/>
      <circle role="img" aria-label="Photo: loaded hot dog on a poppy seed bun" cx="568" cy="772" r="96" fill="url(#foodTone)"/>
    </g>
    <g class="photo-circle">
      <circle cx="1074" cy="704" r="144" fill="var(--ring-blue)"/>
      <circle cx="1074" cy="704" r="141" fill="var(--ring-white)"/>
      <circle role="img" aria-label="Photo: children playing in a splash fountain" cx="1074" cy="704" r="135" fill="url(#fountainTone)"/>
    </g>
  </svg>

  <section class="feature feature--intro">
    <h2 class="feature__title">Bright Lantern</h2>
    <p class="feature__body">Spend the time necessary to consider your business requirements, your needs and your budget yield to your IT services expectations, not what we think you should have.</p>
    <p class="feature__body">Prevent potential down time and data loss disasters from occurring instead of reactively dousing the fire with our computer support</p>
  </section>

  <section class="feature feature--social">
    <h2 class="feature__title">Social Media</h2>
    <p class="feature__body">Spend the time necessary to consider your business requirements, your needs and your budget yield to your IT services expectations, not what we think you should have.</p>
    <p class="feature__body">Prevent potential down time and data loss disasters from occurring instead of reactively dousing the fire with our computer support</p>
  </section>

  <section class="feature feature--location">
    <h2 class="feature__title">Tapped on location</h2>
    <p class="feature__body">Spend the time necessary to consider your business requirements, your needs and your budget yield to your IT services expectations, not what we think you should have.</p>
    <p class="feature__body">Prevent potential down time and data loss disasters from occurring instead of reactively dousing the fire with our computer support</p>
  </section>

  <section class="feature feature--closing">
    <h2 class="feature__title">Some Copy here</h2>
    <p class="feature__body">Spend the time necessary to consider your business requirements, your needs and your budget yield to your IT services expectations, not what we think you should have.</p>
  </section>
</main>
</body>
</html>
```